Cover for book on creating escape rooms for educational purposes

A small business (puzzle chamber academy) needs a book cover design for a new book they are launching as a how-to guide to create educational escape rooms. The target audience is for educators wanting to better engage their students of all ages (Primary, Secondary, Tertiary, Corporate Training).
Book Title: Boundless Classrooms
Sub Title: Harnessing the thrill of puzzle chambers to make teaching unforgettable
Authors: Dr Gavin and Helen Pryce

Book is to be sold on Novamart books as a Lumora eBook and hard copy

Target Market(s)

Educators/Teachers

Industry/Entity Type

Education

Requirements
Must have
• Puzzle Chamber Academy Logo
Should not have
• A focus only on children

```html
<!DOCTYPE html>
<html lang="en">
<head>
<meta charset="utf-8">
<title>Boundless Classrooms – Book Cover</title>
<link href="https://fonts.googleapis.com/css2?family=Bebas+Neue&family=Oswald:wght@500&family=Caladea&display=swap" rel="stylesheet">
<style>
  :root {
    --page-bg: #e9ecee;
    --band-dark: #2b2321;
    --door-blue: #2f5b96;
    --door-blue-deep: #224679;
    --door-blue-light: #3a6aa8;
    --frame-teal: #5fa9c0;
    --frame-shadow: #1d3d66;
    --title-yellow: #fbb732;
    --text-white: #ffffff;
    --keyhole-dark: #1b1b1b;
  }
  * { margin: 0; padding: 0; box-sizing: border-box; }
  html, body {
    width: 1154px; height: 1200px; overflow: hidden;
    background: var(--page-bg);
  }
  .book-cover {
    position: absolute; left: 237px; top: 30px;
    width: 680px; height: 1140px; overflow: hidden;
    background: var(--door-blue);
  }
  .door-wood {
    position: absolute; inset: 0;
    background: linear-gradient(90deg, var(--door-blue-deep) 0%, var(--door-blue) 12%, var(--door-blue-light) 50%, var(--door-blue) 88%, var(--door-blue-deep) 100%);
  }
  .top-band {
    position: absolute; left: 0; top: 0; width: 100%; height: 210px;
    background: linear-gradient(180deg, var(--band-dark) 0%, var(--band-dark) 62%, rgba(43,35,33,0) 100%);
  }
  .publisher-mark {
    position: absolute; left: 0; top: 64px; width: 100%;
    display: flex; justify-content: center; align-items: center; gap: 14px;
  }
  .publisher-dot {
    width: 52px; height: 52px; border-radius: 50%;
    background: var(--title-yellow);
  }
  .publisher-name {
    font-family: "Oswald", sans-serif; font-weight: 500;
    font-size: 30px; letter-spacing: 1px; text-transform: uppercase;
    color: var(--title-yellow);
  }
  .door-panel {
    position: absolute; left: 82px; top: 210px; width: 516px; height: 960px;
    border-left: 9px solid var(--frame-teal);
    border-right: 9px solid var(--frame-teal);
    border-top: 9px solid var(--frame-teal);
    box-shadow: inset 6px 6px 0 var(--frame-shadow), inset -3px 0 0 var(--frame-shadow);
  }
  .title {
    position: absolute; left: 0; top: 262px; width: 100%;
    text-align: center; font-family: "Bebas Neue", sans-serif;
    font-weight: 400; line-height: 0.9;
  }
  .title-top { display: block; font-size: 138px; color: var(--title-yellow); }
  .title-bottom { display: block; font-size: 112px; color: var(--text-white); margin-top: 4px; }
  .subtitle {
    position: absolute; left: 60px; top: 510px; width: 560px;
    text-align: center; font-family: "Oswald", sans-serif; font-weight: 500;
    font-size: 22px; line-height: 1.3; letter-spacing: 0.5px;
    text-transform: uppercase; color: var(--text-white);
  }
  .subtitle .accent { color: var(--title-yellow); }
  .keyhole-area {
    position: absolute; left: 218px; top: 620px; width: 244px; height: 420px;
    border-radius: 12px;
    background: radial-gradient(ellipse at 50% 45%, var(--keyhole-dark) 0%, var(--keyhole-dark) 45%, var(--door-blue-deep) 100%);
  }
  .authors {
    position: absolute; left: 0; bottom: 22px; width: 100%;
    text-align: center; font-family: "Caladea", serif;
    font-size: 38px; color: var(--text-white);
  }
</style>
</head>
<body>
  <main class="book-cover">
    <div class="door-wood" role="img" aria-label="Blue painted wooden door texture"></div>
    <div class="top-band">
      <div class="publisher-mark">
        <span class="publisher-dot"></span>
        <span class="publisher-name">Puzzle Chamber Academy</span>
      </div>
    </div>
    <div class="door-panel"></div>
    <h1 class="title">
      <span class="title-top">Boundless</span>
      <span class="title-bottom">Classrooms</span>
    </h1>
    <p class="subtitle">Harnessing the thrill of <span class="accent">puzzle chambers</span><br>to make teaching unforgettable</p>
    <div class="keyhole-area" role="img" aria-label="Large black keyhole silhouette cut into the door"></div>
    <p class="authors">Dr Gavin and Helen Pryce</p>
  </main>
</body>
</html>
```